Health care center needs brochure design

We need a set of brochure designs for the 4 sections of our clinic, color coded based on the brand guidelines and with introduced icons to every section. The three sections include Biological Medicine (main medication tool is the IV tool), The Brindle Path program (main medication tool are the detox tools) , the Aesthetics section ( main medication tool is the syringe) and the lab (main tool is the microscope). You can find out more about our sections in the website www.velnortaclinic-example.com. The use of elements of the brand itself such as the lotus is also applicable.

Industry/Entity Type

Health Care

Requirements
Must have
• use of brand identity colors and features
• reflective medical icons
• color coding for each of the 4 sections based on the brand colors
Should not have
• pictures overused by other health care providers

```html
<!DOCTYPE html>
<html lang="en">
<head>
<meta charset="utf-8">
<title>Velnorta Integrated Care Center – Brochure</title>
<link href="https://fonts.googleapis.com/css2?family=Exo+2:wght@500;600&family=Lato:wght@400;700&display=swap" rel="stylesheet">
<style>
  :root{
    --teal:#7cc5a6;
    --teal-dark:#5eb08e;
    --salmon:#f6ad90;
    --coral:#ee4a43;
    --pink:#f2958f;
    --pink-soft:#fde3e4;
    --sky:#c6e2ef;
    --ink:#3d3d3d;
    --ink-soft:#555;
    --paper:#ffffff;
    --stage:#ecebe8;
  }
  *{box-sizing:border-box;margin:0;padding:0}
  html,body{width:1200px;height:1200px;overflow:hidden;background:var(--stage)}
  body{position:relative;font-family:"Lato",sans-serif;color:var(--ink)}
  .spread{position:absolute;left:215px;width:770px;height:544px;background:var(--paper);overflow:hidden;box-shadow:0 2px 10px rgba(0,0,0,.15)}
  .spread--cover{top:36px}
  .spread--inside{top:620px}
  .spread__art{position:absolute;inset:0}
  .spread::after{content:"";position:absolute;left:380px;top:0;width:10px;height:100%;background:linear-gradient(90deg,rgba(0,0,0,0),rgba(0,0,0,.06),rgba(0,0,0,0))}
  .photo{position:absolute}
  .photo--hands{left:400px;top:100px;width:370px;height:320px;background:radial-gradient(ellipse at 60% 45%,#eef0f3 0%,#dfe3e8 45%,#f6f7f9 80%,#fff 100%)}
  .photo--lab{left:0;top:266px;width:385px;height:278px;background:linear-gradient(160deg,#f4f6f8 0%,#dbe3ea 45%,#c9d8e6 75%,#b6cde0 100%)}
  .photo--circle{border-radius:50%;border:6px solid var(--pink)}
  .photo--screen{left:489px;top:392px;width:136px;height:136px;background:radial-gradient(circle at 50% 40%,#cfe1ee,#8fb3cf 70%,#6f97b8)}
  .photo--research{left:597px;top:360px;width:152px;height:152px;background:radial-gradient(circle at 50% 40%,#b5cff0,#3f6fb5 65%,#24477f)}
  .ornament{position:absolute;left:262px;top:350px;width:246px;height:194px;border-radius:20px 20px 0 0;background:linear-gradient(180deg,#8fcfb3,var(--teal));box-shadow:0 0 0 8px #fff}
  .about{position:absolute;left:46px;top:150px;width:294px}
  .section-title{font-family:"Lato",sans-serif;font-weight:700;color:var(--teal);display:flex;align-items:center;gap:8px;font-size:10.5px}
  .section-title em{font-style:normal;color:var(--pink)}
  .section-title::after{content:"";flex:1;height:1px;background:var(--teal)}
  .body-text{font-size:7.6px;line-height:9.8px;text-align:justify;color:var(--ink-soft);margin-top:8px}
  .contact{position:absolute;left:43px;top:450px;list-style:none;font-size:8.6px;color:var(--ink)}
  .contact li{display:flex;gap:8px;align-items:flex-start;margin-bottom:6px;line-height:10.4px}
  .contact svg{width:11px;height:11px;flex:none}
  .social{display:inline-flex;gap:4px;margin-left:20px;vertical-align:middle}
  .social i{display:block;width:11px;height:11px;border-radius:2px;background:var(--coral)}
  .brand{position:absolute;left:430px;top:32px;display:flex;align-items:center;gap:12px}
  .brand__dot{width:46px;height:46px;border-radius:50%;background:var(--salmon)}
  .brand__name{font-family:"Lato",sans-serif;font-weight:700;color:var(--teal);font-size:12px;line-height:13px;letter-spacing:.5px}
  .welcome{position:absolute;left:520px;top:450px;width:246px;text-align:center;font-family:"Exo 2",sans-serif;font-weight:600;font-size:16px;line-height:20px;color:#4a4a4a}
  .welcome strong{color:var(--coral);font-weight:600;display:block}
  .welcome__url{font-family:"Lato",sans-serif;font-weight:400;font-size:7px;letter-spacing:2.2px;color:var(--ink-soft);margin-top:4px}
  .intro{position:absolute;left:19px;top:32px;width:347px}
  .intro__title{font-size:14px;font-weight:700;text-align:center;color:var(--teal);margin-bottom:14px}
  .intro__title em{font-style:normal;color:var(--pink)}
  .intro .body-text{margin-top:9px}
  .factors{position:absolute;left:404px;top:18px;width:346px}
  .factors .body-text{margin-top:0}
  .ticks{list-style:none;font-size:7.6px;color:var(--ink-soft)}
  .ticks li{position:relative;padding-left:15px;line-height:11.8px}
  .ticks li::before{content:"";position:absolute;left:0;top:2.5px;width:6px;height:6px;border:1px solid var(--teal);border-radius:50%}
  .ticks li::after{content:"";position:absolute;left:2.6px;top:4px;width:1.8px;height:3px;border:solid var(--teal);border-width:0 1px 1px 0;transform:rotate(40deg)}
  .ticks li.note::before{border:none;content:"✳";color:var(--teal);font-size:8px;top:-1px;left:0}
  .ticks li.note::after{display:none}
  .cols{display:flex;margin-top:10px}
  .cols .ticks{width:189px}
  .cols .ticks + .ticks{width:157px}
  .restoring{position:absolute;left:385px;top:172px;width:385px;height:88px;background:var(--pink-soft);padding:11px 19px 0}
  .subhead{font-size:10.4px;font-weight:700;color:var(--ink);margin-bottom:6px}
  .restoring .ticks li{line-height:10.6px;margin-bottom:2.8px}
  .conditions{position:absolute;left:404px;top:272px;width:346px}
  .conditions .cols{margin-top:0}
</style>
</head>
<body>

<section class="spread spread--cover" aria-label="Brochure cover spread">
  <svg class="spread__art" viewBox="0 0 770 544" width="770" height="544" aria-hidden="true">
    <defs>
      <linearGradient id="leftPaper" x1="0" y1="0" x2="1" y2="0">
        <stop offset="0" stop-color="#ffffff"/>
        <stop offset="1" stop-color="#f1f2f3"/>
      </linearGradient>
    </defs>
    <rect x="0" y="0" width="385" height="544" fill="url(#leftPaper)"/>
  </svg>
  <div class="photo photo--hands" role="img" aria-label="Photo: doctor's hands sheltering a paper cut-out family"></div>
  <svg class="spread__art" viewBox="0 0 770 544" width="770" height="544" aria-hidden="true">
    <path d="M0,342 C30,410 120,432 257,432 L385,432 L385,544 L0,544Z" fill="var(--salmon)"/>
    <path d="M0,336 C30,404 120,426 257,426" fill="none" stroke="var(--teal)" stroke-width="3"/>
    <path d="M385,432 L521,432 C640,432 745,418 770,364 L770,544 L385,544Z" fill="var(--salmon)"/>
    <path d="M521,426 C640,426 742,412 767,358" fill="none" stroke="var(--teal)" stroke-width="3"/>
  </svg>
  <div class="ornament" role="img" aria-label="Large lotus ornament"></div>

  <div class="brand">
    <div class="brand__dot"></div>
    <div class="brand__name">VELNORTA<br>INTEGRATED<br>CARE CENTER</div>
  </div>

  <div class="about">
    <h2 class="section-title">ABOUT <em>THE CENTER</em></h2>
    <p class="body-text">We are proud to be the first to provide alternative biological medicine in the region integrated with programs that envelope the healing process in a complete cycle touching The Body, The Mind and The Soul. The Center provides access to new ways of healing via Ayurverdic medicine and Aesthetic procedures. It also provides new diagnostics and regime treatments to encompass the needs of your body taking it towards its natural healthy state in a happy purified mind and soul.</p>
    <p class="body-text">Created to be your healing getaway, the center is set to make you feel welcome and at ease from the moment you step in. We wish to ensure your steps towards a better tranformed you starts with a smile. We aim to see you glowing with the beautiful life within you and to guide you bring out the best in your natural self.</p>
  </div>

  <ul class="contact">
    <li><svg viewBox="0 0 12 12"><path d="M6,1 L11.5,6 L10,6 L10,11 L7.3,11 L7.3,8 L4.7,8 L4.7,11 L2,11 L2,6 L0.5,6Z" fill="var(--coral)"/></svg><span>Velnorta Integrated Care Center<br>POBox 40218</span></li>
    <li><svg viewBox="0 0 12 12"><path d="M3,1.2 L4.8,3.6 L3.8,4.8 C4.4,6.2 5.6,7.5 7.2,8.2 L8.4,7.2 L10.8,9 L9.8,10.8 C5.6,10.6 1.4,6.4 1.2,2.2Z" fill="none" stroke="var(--coral)" stroke-width="1"/></svg><span>02-555 0143</span></li>
    <li><svg viewBox="0 0 12 12"><rect x="1" y="2.5" width="10" height="7" fill="none" stroke="var(--coral)" stroke-width="1"/><path d="M1,2.5 L6,6.5 L11,2.5" fill="none" stroke="var(--coral)" stroke-width="1"/></svg><span>info@velnortaclinic-example.com</span></li>
    <li><svg viewBox="0 0 12 12"><circle cx="6" cy="6" r="5" fill="none" stroke="var(--coral)" stroke-width="1"/><ellipse cx="6" cy="6" rx="2.2" ry="5" fill="none" stroke="var(--coral)" stroke-width="1"/><path d="M1,6 L11,6" stroke="var(--coral)" stroke-width="1"/></svg><span>www.velnortaclinic-example.com</span><span class="social" aria-label="Social media"><i></i><i></i></span></li>
  </ul>

  <div class="welcome">
    Welcome to The First and
    <strong>ONLY INTEGRATIVE CENTER</strong>
    of its kind in the Region
    <div class="welcome__url">www.velnortaclinic-example.com</div>
  </div>
</section>

<section class="spread spread--inside" aria-label="Brochure inside spread">
  <div class="photo photo--lab" role="img" aria-label="Photo: three scientists in lab coats working at a microscope"></div>
  <svg class="spread__art" viewBox="0 0 770 544" width="770" height="544" aria-hidden="true">
    <path d="M0,486 C60,520 160,540 250,544 L0,544Z" fill="var(--sky)"/>
    <path d="M0,380 C10,440 40,480 90,500" fill="none" stroke="var(--teal)" stroke-width="2.5"/>
    <path d="M385,506 C470,470 620,500 770,396 L770,544 L385,544Z" fill="var(--sky)"/>
    <path d="M560,498 C650,480 730,450 770,396" fill="none" stroke="var(--teal)" stroke-width="2.5"/>
  </svg>
  <div class="photo photo--circle photo--screen" role="img" aria-label="Photo: scientist viewing a medical body scan on a screen"></div>
  <div class="photo photo--circle photo--research" role="img" aria-label="Photo: researcher in protective gear handling a lab flask"></div>

  <div class="intro">
    <h2 class="intro__title">WHAT IS <em>BIOLOGICAL MEDICINE?</em></h2>
    <p class="body-text">Biological medicine is a holistic approach to health and wellness that allows the human body to maximize its own innate healing powers.One of the most powerful ways to establish health in your life is to live in harmony with your inner rhythms. By reconnecting with our inner rhythmic processes and innate wisdom we will lead ourselves toward a more balanced state of health.</p>
    <p class="body-text">Your internal rhythms are real—as real as your heartbeat, the rise and fall of your breathing and the ebb and flow of your hormones. In fact, all biological functions occur rhythmically. As human beings, we are constantly searching and striving for ways to improve our health and the health of our loved ones. Biological medicine has been providing clients with a uniquely restorative, holistic system, rooted in ancient Eastern and Western traditions and balanced with an exceptional understanding of modern science and medicine.</p>
    <p class="body-text">The wisdoms of age old practices like Ayurveda, Chinese herbalism, homeopathy and natural European remedies, are used to restore bodily harmony. The basic philosophy of Biological Medicine is expressed by its name: “bio-logic”—the logic of nature. The foundation of biological medicine is the body’s own “Knowledge of Life”—the body’s innate wisdom regarding natural forces within and around the individual. Because every person is unique, biological medicine treats the individual, not just the disease. Both the practitioner and client work together to discover and free the body’s own natural way of healing.</p>
  </div>

  <div class="factors">
    <p class="body-text">Biological medicine looks for the underlying source of illness. These root causes may consist of several factors that, over time, can allow disease causing toxins to build up in the body. Some of these underlying factors include:</p>
    <div class="cols">
      <ul class="ticks">
        <li>diet</li><li>food allergies</li><li>intestinal disturbances</li><li>family history</li><li>stress</li><li>aging</li><li>environmental factors</li><li>heavy metals</li>
      </ul>
      <ul class="ticks">
        <li style="margin-bottom:2px">dental disturbances</li><li style="margin-bottom:2px">hyperacidity</li><li style="margin-bottom:2px">trauma</li><li style="margin-bottom:2px">exposure to bacteria or viruses</li><li style="margin-bottom:6px">electromagnetic disturbances</li>
        <li class="note" style="line-height:10px">Without fundamental changes in these root causes, there can be no real healing.</li>
      </ul>
    </div>
  </div>

  <div class="restoring">
    <h3 class="subhead">Restoring the body with biological medicine is done through:</h3>
    <ul class="ticks">
      <li>detoxification,</li>
      <li>rebuilding the digestive system,</li>
      <li>strengthening the immune system and alkalizing your body through diet, to support the proper pH, one of the most important foundations of health</li>
    </ul>
  </div>

  <div class="conditions">
    <h3 class="subhead">Conditions we treat</h3>
    <div class="cols">
      <ul class="ticks">
        <li>Autoimmune Diseases</li><li>Cancer</li><li>Cardiovascular Diseases and Hypertension</li><li>Intestinal and Digestive Disorders</li>
      </ul>
      <ul class="ticks">
        <li>Joint Pain and Bone Health</li><li>Lyme and Chronic Infections</li><li>Metabolic and Degenerative Conditions</li><li>Neurological Disorders</li>
      </ul>
    </div>
  </div>
</section>

</body>
</html>
```